Mattress sale flyer front and back

FLYER SIZE!! front and back!
4.25" X 5.5"
or
10.7cm X 13.9 cm

This flyer needs to show the prices
twin.....$99
full.......$159
queen...$199
king....$299

the phone number........(786)555-0147
the address ..........10420 sw 172st miami fl 33157
if possible a map would be appreciated

possible brands to include.......Dormo, Kellbrook, vale & pruitt, lunadown

ATTACHED IS OUR OLD FLYER WITH OUTDATED INFORMATION, I WOULD LIKE SOMETHING SIMILAR. JUST ADD A LITTLE PRICE LIST AND A MAP

***FRONT AND BACK PLEASE****

```html
<!DOCTYPE html>
<html lang="en">
<head>
<meta charset="utf-8">
<title>Coral Rest Outlet – Mattress Sale Flyer, Front and Back</title>
<link href="https://fonts.googleapis.com/css2?family=Playfair+Display:wght@400;700&family=Arimo:wght@400;700&display=swap" rel="stylesheet">
<style>
  :root{
    --stage:#1c1c1c;
    --paper:#ffffff;
    --teal:#00b0c8;
    --charcoal:#58585a;
    --ink:#3e3e40;
    --yellow:#f5d327;
    --map:#e9e5dc;
    --frame:#4a4a4c;
  }
  *{box-sizing:border-box;margin:0;padding:0}
  html,body{width:1200px;height:1000px;overflow:hidden;background:var(--stage)}
  .sheet{position:relative;width:1200px;height:1000px;display:flex;align-items:center;justify-content:center;gap:30px}
  .flyer{position:relative;width:560px;height:460px;background:var(--paper);overflow:hidden;box-shadow:0 10px 30px rgba(0,0,0,.5)}
  .flyer__shapes{position:absolute;inset:0}
  .brandmark{position:absolute;display:flex;align-items:center;gap:10px;font-family:"Playfair Display",serif;font-weight:400;font-size:30px;color:var(--ink);white-space:nowrap}
  .brandmark__dot{width:16px;height:16px;border-radius:50%;background:var(--teal)}
  .front .brandmark{left:60px;top:48px}
  .back .brandmark{left:250px;top:38px}

  .tagline{position:absolute;left:30px;top:258px;color:#fff;font-family:"Arimo",sans-serif;line-height:1}
  .tagline__big{font-size:30px;display:block}
  .tagline__small{font-size:22px;display:inline-block;margin-top:4px}
  .badge{display:inline-flex;align-items:center;justify-content:center;background:var(--yellow);border-radius:50%;color:var(--ink);font-family:"Playfair Display",serif;font-weight:700}
  .tagline .badge{width:92px;height:44px;font-size:22px;margin-left:4px;vertical-align:middle}
  .photo{position:absolute}
  .front .photo{left:38px;top:330px;width:200px;height:120px;border-radius:4px;background:linear-gradient(180deg,#f4f4f2,#cfcfcb)}

  .price-list{position:absolute;left:305px;top:140px;width:205px;border:2px solid var(--yellow);border-radius:10px;padding:8px 18px;font-family:"Arimo",sans-serif;color:#fff;font-size:19px}
  .price-list__row{display:flex;justify-content:space-between;padding:5px 0;border-bottom:1px dashed rgba(255,255,255,.8)}
  .price-list__row:last-child{border-bottom:none}
  .slogan{position:absolute;left:275px;top:328px;font-family:"Playfair Display",serif;font-weight:700;font-size:20px;color:var(--yellow);white-space:nowrap}
  .brand-strip{position:absolute;left:250px;top:372px;width:310px;height:46px;background:var(--paper);display:flex;align-items:center;justify-content:space-around;padding:0 8px;font-family:"Arimo",sans-serif;font-size:13px;font-weight:700;color:var(--charcoal)}

  .back .badge{position:absolute;left:30px;top:108px;width:120px;height:48px;font-size:20px;z-index:2}
  .back .photo{left:40px;top:140px;width:250px;height:190px;border:6px solid var(--frame);background:linear-gradient(180deg,#ffffff,#dcdcd8)}
  .phone{position:absolute;left:44px;top:350px;font-family:"Playfair Display",serif;font-weight:700;font-size:30px;color:#fff}
  .web{position:absolute;left:30px;top:404px;font-family:"Arimo",sans-serif;font-size:17px;color:#fff}
  .map{position:absolute;left:270px;top:115px;width:290px;height:345px;background:linear-gradient(160deg,#ece8df,#dedad0)}
  .address{position:absolute;left:320px;top:372px;width:222px;padding:6px 10px;background:rgba(255,255,255,.88);font-family:"Playfair Display",serif;font-weight:700;font-size:20px;line-height:1.25;color:var(--ink)}
  .pin{position:absolute;left:405px;top:245px}
</style>
</head>
<body>
<main class="sheet">

  <section class="flyer front" aria-label="Flyer front">
    <svg class="flyer__shapes" width="560" height="460" viewBox="0 0 560 460" aria-hidden="true">
      <path d="M0 250 Q150 200 300 238 L300 460 L0 460 Z" fill="var(--teal)"/>
      <path d="M245 460 C195 300 235 125 390 112 L560 112 L560 460 Z" fill="var(--charcoal)"/>
    </svg>
    <div class="brandmark"><span class="brandmark__dot"></span>Coral Rest Outlet</div>

    <p class="tagline"><span class="tagline__big">Recharge</span><span class="tagline__small">and</span><span class="badge">SAVE</span></p>
    <div class="photo" role="img" aria-label="Photo of two white pillow-top mattress sets"></div>

    <div class="price-list">
      <div class="price-list__row"><span>Twin</span><span>$99</span></div>
      <div class="price-list__row"><span>Full</span><span>$159</span></div>
      <div class="price-list__row"><span>Queen</span><span>$199</span></div>
      <div class="price-list__row"><span>King</span><span>$299</span></div>
    </div>
    <p class="slogan">Lowest Prices. Best Brands.</p>
    <div class="brand-strip">
      <span>Dormo</span><span>Kellbrook</span><span>Vale &amp; Pruitt</span><span>Lunadown</span>
    </div>
  </section>

  <section class="flyer back" aria-label="Flyer back">
    <div class="map" role="img" aria-label="Street map showing the store location"></div>
    <svg class="flyer__shapes" width="560" height="460" viewBox="0 0 560 460" aria-hidden="true">
      <path d="M0 100 C130 85 255 110 300 200 C340 285 320 400 285 460 L0 460 Z" fill="var(--teal)"/>
    </svg>
    <div class="brandmark"><span class="brandmark__dot"></span>Coral Rest Outlet</div>

    <span class="badge">Call Now!</span>
    <div class="photo" role="img" aria-label="Photo of a mattress with its layers shown apart"></div>
    <p class="phone">(786) 555-0147</p>
    <p class="web">www.coralrestoutlet.com</p>

    <svg class="pin" width="14" height="20" viewBox="0 0 14 20" aria-hidden="true">
      <path d="M7 0C3 0 0 3 0 7c0 5 7 13 7 13s7-8 7-13c0-4-3-7-7-7z" fill="#d9463b"/>
      <circle cx="7" cy="7" r="2.5" fill="#8e2a23"/>
    </svg>
    <p class="address">10420 SW 172ST<br>MIAMI FL 33157</p>
  </section>

</main>
</body>
</html>
```